New Business Card (to reflect updated website content and graphics)

I changed some text and graphics on my website, so I need a new business card.

Target Market(s)

Mostly women, ages 30 - 60.

Industry/Entity Type

Life Coaching

Contact Information for Business Card

Included in attached Word document

Font styles to use
Sans Serif

Requirements
Must have
• I am not a creative person, so I will defer to designer. Take a look at my website, and you can get a feel for me, my style, and my target audience. Thank You!

My 3 branding colors are included in attached Word document.

```html
<!DOCTYPE html>
<html lang="en">
<head>
<meta charset="utf-8">
<title>Harbor Heart Coaching – Business Card</title>
<link rel="stylesheet" href="https://fonts.googleapis.com/css2?family=Source+Sans+3:wght@400;600&family=Oswald:wght@500&family=Lobster+Two:ital,wght@1,700&display=swap">
<style>
  :root {
    --teal: #2a8fa8;
    --teal-soft: #d3e9ef;
    --teal-softer: #e6f2f5;
    --coral: #e8786a;
    --ink: #2b2b2b;
    --card: #f4f4f4;
    --backdrop: #e2e2e2;
    --backdrop-light: #f1f1f1;
  }
  * { margin: 0; padding: 0; box-sizing: border-box; }
  html, body { width: 1200px; height: 960px; overflow: hidden; }
  body {
    position: relative;
    background: radial-gradient(ellipse at center, var(--backdrop-light) 0%, var(--backdrop) 70%);
    font-family: "Source Sans 3", "Source Sans Pro", sans-serif;
  }
  .card {
    position: absolute;
    left: 297px;
    width: 602px;
    height: 344px;
    background: var(--card);
    box-shadow: 2px 3px 6px rgba(0,0,0,0.35);
    overflow: hidden;
  }
  .card--front { top: 110px; }
  .card--back { top: 507px; }

  .word-cloud {
    position: absolute;
    left: 165px; top: 40px;
    width: 276px; height: 242px;
    background: linear-gradient(180deg, var(--teal-soft) 0%, var(--teal-softer) 100%);
  }
  .front-headline {
    position: absolute;
    left: 165px; top: 100px;
    width: 276px;
    text-align: center;
    font-family: "Oswald", sans-serif;
    font-weight: 500;
    font-size: 36px;
    line-height: 44px;
    letter-spacing: -0.5px;
    color: var(--coral);
  }
  .front-tagline {
    position: absolute;
    left: 0; right: 0; top: 283px;
    text-align: center;
    font-family: "Lobster Two", cursive;
    font-style: italic; font-weight: 700;
    font-size: 26px;
    color: var(--teal);
  }
  .front-tagline .accent { color: var(--coral); }

  .brand-name {
    position: absolute;
    right: 40px; top: 60px;
    font-size: 30px; font-weight: 400;
    color: var(--teal);
    text-align: right;
    line-height: 1.1;
    letter-spacing: 1px;
  }
  .coach { position: absolute; left: 39px; top: 139px; }
  .coach-name {
    font-size: 22px; font-weight: 600;
    color: var(--teal);
    line-height: 26px;
  }
  .coach-titles {
    list-style: none;
    font-size: 16px; color: var(--ink);
    line-height: 20px;
  }
  .contact {
    position: absolute;
    left: 39px; top: 251px;
    list-style: none;
    font-size: 16px; color: var(--ink);
    line-height: 20px;
  }
  .contact li { display: flex; align-items: center; gap: 7px; }
  .contact svg { width: 14px; height: 14px; flex: none; }
  .swoosh { position: absolute; left: 0; top: 0; width: 602px; height: 344px; }
</style>
</head>
<body>

<section class="card card--front" aria-label="Card front">
  <div class="word-cloud" role="img" aria-label="Heart-shaped word cloud of coaching themes such as hope, love, joy, clarity and peace"></div>
  <p class="front-headline">FEEL BETTER, LIVE WELL</p>
  <p class="front-tagline">True Happiness <span class="accent">Comes From Within</span></p>
</section>

<section class="card card--back" aria-label="Card back">
  <svg class="swoosh" viewBox="0 0 602 344" aria-hidden="true">
    <path d="M331 344 Q510 292 602 166 L602 344 Z" fill="var(--coral)"/>
    <path d="M385 344 Q545 292 602 160 L602 344 Z" fill="var(--teal)" stroke="#ffffff" stroke-width="2"/>
  </svg>

  <p class="brand-name">Harbor Heart<br>Coaching</p>

  <div class="coach">
    <h1 class="coach-name">Marla Kestrel</h1>
    <ul class="coach-titles">
      <li>Certified Professional Life Coach</li>
      <li>Health &amp; Wellness Coach</li>
      <li>Advanced Grief Support Specialist</li>
    </ul>
  </div>

  <ul class="contact">
    <li>
      <svg viewBox="0 0 16 16" aria-hidden="true"><path d="M3.6 1.2 L6 3.6 L4.6 5.4 C5.4 7.4 8.6 10.6 10.6 11.4 L12.4 10 L14.8 12.4 L13.2 14.6 C7.6 14.2 1.8 8.4 1.4 2.8 Z" fill="var(--teal)"/></svg>
      (555) 014-2290
    </li>
    <li>
      <svg viewBox="0 0 16 16" aria-hidden="true"><rect x="1.5" y="3.5" width="13" height="9" fill="none" stroke="var(--teal)" stroke-width="1.5"/><path d="M1.5 3.5 L8 9 L14.5 3.5" fill="none" stroke="var(--teal)" stroke-width="1.5"/></svg>
      marla@harborheartcoaching.com
    </li>
    <li>
      <svg viewBox="0 0 16 16" aria-hidden="true"><g fill="none" stroke="var(--teal)" stroke-width="1.2"><circle cx="8" cy="8" r="6.3"/><ellipse cx="8" cy="8" rx="2.8" ry="6.3"/><path d="M1.7 8 H14.3 M2.8 4.6 H13.2 M2.8 11.4 H13.2"/></g></svg>
      www.harborheartcoaching.com
    </li>
  </ul>
</section>

</body>
</html>
```